Design a poster that illustrates the six central pillars of our school district's efforts with students. The attached PDF outlines the six main competencies we aim for students to possess upon graduation. Each of the 6 has 3 bullet points for the poster as well. The title is "Profile of a Kestrel". Our mascot is this attached winged wheel. The overall concept is that staff take kids when they are young and develop these 6 things when they graduate. Our colors are navy, red, and white. We will make this poster in a variety of sizes in offices, classrooms, and in digital spaces as well. On the PDF - ignore the column that says "Synthesis". That has nothing to do with this poster.

The district is Harlow Creek Public Schools https://www.harlowcreek-schools.example/

```html
<!DOCTYPE html>
<html lang="en">
<head>
<meta charset="utf-8">
<title>Profile of a Kestrel — Harlow Creek Public Schools</title>
<link rel="stylesheet" href="https://fonts.googleapis.com/css2?family=Anton&family=Oswald:wght@600&family=Montserrat:wght@500&display=swap">
<style>
  :root {
    --navy: #213047;
    --red: #a01c24;
    --white: #ffffff;
    --ink: #1f2733;
  }
  * { margin: 0; padding: 0; box-sizing: border-box; }
  html, body { width: 848px; height: 1200px; overflow: hidden; background: var(--white); }
  .poster { position: relative; width: 848px; height: 1200px; background: var(--white); overflow: hidden; }

  .navy-panel { position: absolute; left: 0; top: 0; width: 411px; height: 1005px; background: var(--navy); }

  .title {
    position: absolute; top: 48px;
    font-family: "Anton", sans-serif; font-weight: 400;
    font-size: 98px; line-height: 1; letter-spacing: -1px;
    color: var(--red);
    -webkit-text-stroke: 3px var(--white);
    paint-order: stroke fill;
    text-shadow: 0 4px 8px rgba(0,0,0,0.25);
  }
  .title-left { left: 32px; }
  .title-right { left: 426px; }

  .pillar-heading {
    position: absolute;
    font-family: "Oswald", sans-serif; font-weight: 600;
    font-size: 54px; line-height: 1; letter-spacing: -0.5px;
  }
  .on-navy .pillar-heading { color: var(--white); }
  .on-white .pillar-heading { color: var(--red); }

  .traits {
    position: absolute; list-style: none;
    font-family: "Montserrat", sans-serif; font-weight: 500;
    font-size: 16px; line-height: 19.4px; letter-spacing: 0.2px;
  }
  .traits::before {
    content: ""; position: absolute; left: 6px; top: 8px; bottom: -4px;
    width: 1px; background: currentColor; opacity: 0.8;
  }
  .traits li { position: relative; padding-left: 34px; margin-bottom: 19px; }
  .traits li:last-child { margin-bottom: 0; }
  .check {
    position: absolute; left: 0; top: 2px; width: 13px; height: 13px;
  }
  .check::after {
    content: ""; position: absolute; left: 4px; top: 1px;
    width: 3px; height: 7px; border-right: 1.6px solid; border-bottom: 1.6px solid;
    transform: rotate(40deg);
  }
  .on-navy .traits { color: var(--white); }
  .on-navy .check { border: 1.2px solid var(--white); background: var(--navy); }
  .on-navy .check::after { border-color: var(--white); }
  .on-white .traits { color: var(--ink); }
  .on-white .check { background: var(--navy); }
  .on-white .check::after { border-color: var(--white); }

  .left-col .pillar-heading, .left-col .traits { left: 34px; }
  .left-col .traits { width: 370px; }
  .right-col .pillar-heading, .right-col .traits { left: 428px; }
  .right-col .traits { width: 400px; }

  .footer-navy { position: absolute; left: 0; top: 1093px; width: 848px; height: 82px; background: var(--navy); }
  .footer-red { position: absolute; left: 200px; top: 1068px; width: 648px; height: 96px; background: var(--red); }
  .mark-circle {
    position: absolute; left: 144px; top: 1060px; width: 88px; height: 88px;
    border-radius: 50%; background: var(--white); border: 4px solid var(--navy);
  }
  .district {
    position: absolute; left: 290px; top: 1084px; color: var(--white);
    font-family: "Montserrat", sans-serif; font-weight: 500;
  }
  .district-name { font-size: 29px; line-height: 1.2; letter-spacing: 0.2px; }
  .district-tagline { font-size: 25px; line-height: 1.3; }
</style>
</head>
<body>
<main class="poster">
  <div class="navy-panel"></div>

  <h1 class="title title-left">PROFILE OF</h1>
  <div class="title title-right" aria-hidden="true">A KESTREL</div>

  <section class="left-col on-navy">
    <h2 class="pillar-heading" style="top:176px">Communicator</h2>
    <ul class="traits" style="top:248px">
      <li><span class="check"></span>Expresses ideas clearly and<br>respectfully (written &amp; verbal).</li>
      <li><span class="check"></span>Listens actively and understands<br>diverse perspectives.</li>
      <li><span class="check"></span>Adjusts communication to suit the<br>audience and context.</li>
    </ul>

    <h2 class="pillar-heading" style="top:444px">Critical Thinker</h2>
    <ul class="traits" style="top:513px">
      <li><span class="check"></span>Questions, analyzes, and evaluates<br>information from multiple sources.</li>
      <li><span class="check"></span>Identifies and solves complex problems<br>creatively.</li>
      <li><span class="check"></span>Uses evidence and diverse perspectives<br>to form reasoned conclusions and make<br>informed decisions.</li>
    </ul>

    <h2 class="pillar-heading" style="top:718px">Responsible</h2>
    <ul class="traits" style="top:799px">
      <li><span class="check"></span>Takes ownership of actions, choices,<br>and commitments now and in future<br>aspirations.</li>
      <li><span class="check"></span>Takes pride in managing time,<br>resources, and self while striving to<br>meet high expectations.</li>
      <li><span class="check"></span>Acts with integrity while advocating<br>for themselves and others.</li>
    </ul>
  </section>

  <section class="right-col on-white">
    <h2 class="pillar-heading" style="top:176px">Adaptable</h2>
    <ul class="traits" style="top:248px">
      <li><span class="check"></span>Responds productively to new situations,<br>challenges, and constructive feedback.</li>
      <li><span class="check"></span>Learns from new experiences and applies<br>prior knowledge in an ever-changing world.</li>
      <li><span class="check"></span>Adjusts behavior and approach to engage<br>effectively with diverse groups and<br>environments.</li>
    </ul>

    <h2 class="pillar-heading" style="top:460px">Collaborator</h2>
    <ul class="traits" style="top:529px">
      <li><span class="check"></span>Demonstrates strong teamwork by<br>contributing effectively and cooperatively<br>toward shared goals.</li>
      <li><span class="check"></span>Listens actively and values diverse ideas<br>and perspectives.</li>
      <li><span class="check"></span>Engages respectfully, knowing when to<br>compromise, support, or take the lead.</li>
    </ul>

    <h2 class="pillar-heading" style="top:734px">Compassionate</h2>
    <ul class="traits" style="top:818px">
      <li><span class="check"></span>Understands and acknowledges others'<br>feelings, perspectives, and experiences.</li>
      <li><span class="check"></span>Responds with kindness, patience,<br>empathy, and support.</li>
      <li><span class="check"></span>Seeks to connect with others, contribute<br>positively to their community, and<br>maintain their own well-being.</li>
    </ul>
  </section>

  <footer>
    <div class="footer-navy"></div>
    <div class="footer-red"></div>
    <div class="mark-circle"></div>
    <div class="district">
      <p class="district-name">Harlow Creek Public Schools</p>
      <p class="district-tagline">Excellence in Academics, Arts &amp; Athletics</p>
    </div>
  </footer>
</main>
</body>
</html>
```